Lumenvale Electrics website design

Electrical contractor in Perth that services the domestic and commercial markets. our services include but not limited to:

New Home Installations and Design
Commercial Shop Fit Outs
Rewires
Renovations
Switchboard Upgrades
Kitchen and Bathroom Renovations
RCD'S (Safety Switches)
Smoke Alarms
Power points
Security Lighting
Energy Efficient LED Lighting Designs
Garden Lighting
Downlights
General Electrical Maintenance
TV and Phone Points
Home Theatre Installs
Safety Certificates
24hr Call out service
Electric Hot Water Units
Credit cards accepted

www.facebook.com/lumenvaleelectrics

Industry/Entity Type

Contractor

Number of Pages Required

5+ page

Font styles to use
Sans Serif

Colors
acd037
fbee3e

Requirements
Must have
• contact page, services page, about us, careers page, somewhere I can put some testimonials, somewhere potential clients can book our services online, on the homepage somewhere showing that we can provide 24/7 emergency service
Nice to have
• icon stating that we accept all major credit cards

```html
<!DOCTYPE html>
<html lang="en">
<head>
<meta charset="utf-8">
<title>Lumenvale Electrics</title>
<link rel="stylesheet" href="https://fonts.googleapis.com/css2?family=Oswald:wght@300;400&family=Open+Sans:wght@400;600;700&display=swap">
<style>
:root{
  --blue:#0e4f8c;
  --lime:#d6d83a;
  --grey:#555a60;
  --light:#c9cbce;
  --band:#f7f7f8;
  --line:#e6e6e6;
}
*{margin:0;padding:0;box-sizing:border-box}
html,body{width:1200px;height:1049px;overflow:hidden;background:#fff}
body{position:relative;font-family:"Oswald",sans-serif;color:var(--grey)}
.abs{position:absolute}

.brand{left:171px;top:28px;display:flex;align-items:center;gap:12px}
.brand-dot{width:22px;height:22px;border-radius:50%;background:var(--blue)}
.brand-name{font-family:"Oswald",sans-serif;font-weight:300;font-size:34px;line-height:1;color:var(--lime)}
.brand-reg{left:350px;top:90px;font-family:"Open Sans",sans-serif;font-size:6px;line-height:8px;color:var(--blue)}

.member-badge{left:694px;top:30px;width:104px;height:28px;background:#e9edf1;border-radius:3px}
.divider{left:808px;top:30px;width:1px;height:30px;background:var(--line)}
.hours-badge{left:823px;top:27px;width:44px;height:34px;border-radius:50%;background:#e2453a}
.phone{left:875px;top:20px;font-weight:300;font-size:38px;letter-spacing:-1px;color:var(--grey)}

.nav{right:171px;top:84px;display:flex;gap:14px;font-size:15px;letter-spacing:-0.8px;color:var(--grey);text-transform:uppercase}
.nav a{color:inherit;text-decoration:none;position:relative}
.nav a.active{color:var(--lime)}
.nav a.active::after{content:"";position:absolute;left:-10px;right:-10px;top:38px;height:2px;background:var(--lime)}

.hero{left:0;top:123px;width:1200px;height:473px;background:linear-gradient(100deg,#c3c8d2 0%,#dfe2e9 40%,#e9ebf0 60%,#d7dbe3 100%)}
.hero-photo{left:590px;top:123px;width:475px;height:473px;background:linear-gradient(180deg,#d9dce3 0%,#6a82c9 45%,#3551b0 100%);border-radius:180px 180px 0 0;opacity:.85}
.slider-dots{left:172px;top:204px;display:flex;gap:3px}
.slider-dots span{width:12px;height:11px;background:#9aa0a8}
.slider-dots span.on{background:#4a7eb0}
.hero-title{left:170px;top:236px;font-weight:300;font-size:58px;letter-spacing:-1px;color:var(--blue);line-height:1.05;white-space:nowrap;transform:scaleX(.78);transform-origin:left top}
.hero-text{left:172px;top:310px;width:390px;font-weight:300;font-size:18px;line-height:21px;letter-spacing:-.5px;color:#3b3f44}
.btn-book{left:171px;top:458px;width:227px;height:50px;border:1px solid var(--blue);color:var(--blue);font-size:21px;letter-spacing:-.5px;display:flex;align-items:center;justify-content:center}

.services{left:171px;top:626px;display:flex;gap:10px}
.service{width:135px;height:170px;background:#fbfbfb;display:flex;flex-direction:column;align-items:center;padding-top:32px;font-family:"Open Sans",sans-serif;font-weight:600;font-size:10.5px;line-height:12.5px;text-align:center;text-transform:uppercase;color:#d4d6d8}
.service svg{width:62px;height:62px;margin-bottom:18px;stroke:#dcdee0;fill:none;stroke-width:3}
.service.active{background:#f5f6f7;color:var(--blue)}
.service.active svg{stroke:var(--blue);fill:var(--blue)}
.arrow{width:32px;height:32px;border-radius:50%;border:1px solid #cfd6de;background:#fff;display:flex;align-items:center;justify-content:center;top:694px}
.arrow svg{width:12px;height:12px;fill:none;stroke-width:3}

.band{left:0;top:821px;width:1200px;height:123px;background:var(--band)}
.feature{top:866px;display:flex;align-items:center;gap:8px;font-size:18px;letter-spacing:-.5px;color:var(--blue)}
.feature svg{width:36px;height:34px}
.social{top:871px;width:25px;height:25px;border-radius:3px}

.footer-brand{left:537px;top:962px;display:flex;align-items:center;gap:8px}
.footer-brand .brand-dot{width:12px;height:12px}
.footer-brand .brand-name{font-size:22px}
.copyright{left:0;width:1200px;top:1012px;text-align:center;font-family:"Open Sans",sans-serif;font-size:10px;letter-spacing:-.3px;color:#9a9da1}
</style>
</head>
<body>

<header>
  <div class="abs brand"><span class="brand-dot"></span><span class="brand-name">Lumenvale Electrics</span></div>
  <div class="abs brand-reg">EC 20461<br>ABN 12345678901</div>
  <div class="abs member-badge" role="img" aria-label="Trade association member badge"></div>
  <div class="abs divider"></div>
  <div class="abs hours-badge" role="img" aria-label="24/7 service badge"></div>
  <div class="abs phone">10 20 30 40 50</div>
  <nav class="abs nav">
    <a class="active">Home</a><a>Services</a><a>About Us</a><a>Careers</a><a>Testimonials</a><a>Online Booking</a><a>Contact</a>
  </nav>
</header>

<section>
  <div class="abs hero" role="img" aria-label="Soft-focus hanging light bulbs background"></div>
  <div class="abs hero-photo" role="img" aria-label="Electrician in blue overalls carrying a coil of conduit and a multimeter"></div>
  <div class="abs slider-dots"><span></span><span></span><span class="on"></span><span></span><span></span></div>
  <h1 class="abs hero-title">LUMENVALE ELECTRICS</h1>
  <p class="abs hero-text">Lorem ipsum dolor sit amet, consectetuer adipiscing elit, sed diam nonummy nibh euismod tincidunt ut laoreet dolore magna aliquam erat volutpat. Ut wisi enim ad minim veniam, quis nostrud exerci tation ullamcorper suscipit lobortis nisl ut aliquip ex ea commodo consequat.</p>
  <div class="abs btn-book">BOOK NOW</div>
</section>

<section>
  <div class="abs arrow" style="left:124px"><svg viewBox="0 0 12 12" stroke="#0e4f8c"><path d="M8 1 3 6l5 5"/></svg></div>
  <div class="abs arrow" style="left:1045px;border-color:#eceff2"><svg viewBox="0 0 12 12" stroke="#d5d8dc"><path d="M4 1l5 5-5 5"/></svg></div>
  <div class="abs services">
    <div class="service"><svg viewBox="0 0 62 62"><path d="M10 30 30 12l20 18v20H10z"/><path d="M24 50V36h12v14"/></svg>New Home<br>Installations<br>and Design</div>
    <div class="service active"><svg viewBox="0 0 62 62"><rect x="6" y="6" width="50" height="8" stroke="none"/><path d="M4 16h54v10H4z" stroke="none"/><path d="M9 28h44v28H9z" fill="none" stroke-width="6"/><path d="M28 31v22" stroke-width="6"/></svg>Commercial<br>Shop Fit Outs</div>
    <div class="service"><svg viewBox="0 0 62 62"><rect x="5" y="8" width="52" height="46" rx="4"/><path d="M8 31h16M24 24h12v14H24zM36 27h10M36 35h10"/></svg>Rewires</div>
    <div class="service"><svg viewBox="0 0 62 62"><circle cx="31" cy="31" r="24"/><path d="M24 26a7 7 0 1 1 14 0c0 5-4 6-4 11h-6c0-5-4-6-4-11zM27 41h8"/></svg>Renovations</div>
    <div class="service"><svg viewBox="0 0 62 62"><rect x="6" y="6" width="50" height="18"/><rect x="6" y="30" width="50" height="18"/><path d="M8 56h46" stroke-dasharray="5 4"/></svg>Switchboard<br>Upgrades</div>
    <div class="service"><svg viewBox="0 0 62 62"><path d="M4 32h54v22H4zM44 12h14v20M14 32V20h8v12"/><path d="M22 40h16v8H22z"/></svg>Kitchen and<br>Bathroom<br>Renovations</div>
  </div>
</section>

<section>
  <div class="abs band"></div>
  <div class="abs feature" style="left:173px">
    <svg viewBox="0 0 36 34" fill="none" stroke="#0e4f8c" stroke-width="2.5"><circle cx="19" cy="17" r="14"/><path d="M3 14l3 4 3-4"/></svg>24/7 EMERGENCY SERVICE
  </div>
  <div class="abs feature" style="left:457px">
    <svg viewBox="0 0 36 34" fill="none" stroke="#0e4f8c" stroke-width="2.5"><path d="M3 18 16 6l14 14-13 12z"/><path d="M14 20l6 6 14-20" stroke="#d6d83a" stroke-width="4"/></svg>WE ACCEPT ALL MAJOR CREDIT CARDS
  </div>
  <div class="abs feature" style="left:794px">
    <svg viewBox="0 0 36 34" fill="#0e4f8c"><rect x="3" y="6" width="24" height="26" rx="2"/><rect x="7" y="14" width="4" height="4" fill="#fff"/><rect x="13" y="14" width="4" height="4" fill="#fff"/><rect x="19" y="14" width="4" height="4" fill="#fff"/><rect x="7" y="22" width="4" height="4" fill="#fff"/><rect x="13" y="22" width="4" height="4" fill="#fff"/><rect x="19" y="22" width="4" height="4" fill="#fff"/></svg>BOOK NOW!
  </div>
  <div class="abs social" style="left:967px;background:#3b5a9a" role="img" aria-label="Social network link"></div>
  <div class="abs social" style="left:1002px;background:#2aa3d8" role="img" aria-label="Social network link"></div>
</section>

<footer>
  <div class="abs footer-brand"><span class="brand-dot"></span><span class="brand-name">Lumenvale Electrics</span></div>
  <p class="abs copyright">© 2014 Lumenvale Electric . Inc All Rights Reserved.</p>
</footer>

</body>
</html>
```